Website for the posting of RFQ from companies

BRIGHTQUAY, a website for posting RFQ from government and companies.
Slogan: Promoting ethical and transparent business practices

Designed in HTML5 and responsive.
Government and companies can upload RFQ (request for quotation) advertisements through a back-end which can be searchable by companies interested in submitting quotes to the companies.

Companies once registered, get a username and logon to access back-end to load their advertisements for RFQ.

Users/ entrepreneurs also register and based on their subscription can access certain advertised RFQ information.

Also a platform where companies can notify other businesses of their commodities on hand. Example small mining company, small fishing company, farm growing fruits and veggies.

Weekly newsletter with latest uploaded RFQ information sent to users.
RFQ advert should display how often it was viewed. also display a button to contact company for more information.

Users register to receive sms and email notification when tenders of interest posted in their categories/ industry of interest.

Competitors:
Ko-offerhub.co.za
Bidvaultz.gov.za
Quickbidboard.co.za
Offerspyx.co.za
Marketvine.net

Attached find a detailed brief with more information and websites of my competitors.

Target Market(s)

Business people

Industry/Entity Type

Business

Coding

Coded - Design and coding required

Number of Pages Required

5+ page

Font styles to use
Sans Serif

Requirements
Must have
• simple clean design
• Html5
• Responsive
Nice to have
• Better and improved Design compared to my competitors
• Use of African models in pictures
Should not have
• dark background

```html
<!DOCTYPE html>
<html lang="en">
<head>
<meta charset="utf-8">
<title>Brightquay Trading</title>
<link href="https://fonts.googleapis.com/css2?family=Open+Sans:wght@400;600;700&display=swap" rel="stylesheet">
<style>
:root{
  --navy:#0d3356;
  --navy-deep:#082540;
  --blue:#1c7fbf;
  --blue-light:#2f93d3;
  --ink:#1f2a36;
  --text:#6a6f75;
  --grey:#c8c9cb;
  --line:#e0e2e5;
  --white:#fff;
}
*{margin:0;padding:0;box-sizing:border-box}
html,body{width:757px;height:1200px;overflow:hidden;background:var(--white);font-family:"Open Sans",sans-serif;color:var(--text)}
.page{position:relative;width:757px;height:1200px}
.abs{position:absolute}
.logo{left:61px;top:17px;font-size:21px;font-weight:700;color:var(--navy)}
.lang{left:486px;top:25px;font-size:7px;color:#555}
.btn{display:flex;align-items:center;justify-content:center;font-size:8px;color:var(--white)}
.login{left:574px;top:21px;width:60px;height:18px;background:#9a9ea3}
.join{left:636px;top:21px;width:58px;height:18px;background:var(--blue)}
.nav{left:62px;top:60px;width:632px;height:28px;background:var(--navy);display:flex}
.nav a{flex:1;display:flex;align-items:center;justify-content:center;font-size:8px;color:var(--white);text-decoration:none;border-right:1px solid #0a2a47}
.nav a.active{background:var(--blue);flex:0 0 68px}
.hero{left:62px;top:98px;width:632px;height:308px;background:radial-gradient(ellipse at 50% 35%,#2a74ad 0%,#10497a 45%,#062a4b 100%)}
.panel{left:80px;top:105px;width:468px;height:108px;background:rgba(210,220,230,.82)}
.panel h2{position:absolute;top:22px;width:100%;text-align:center;font-size:15px;font-weight:400;color:var(--navy)}
.field{position:absolute;top:56px;height:21px;background:var(--white);font-size:7px;color:#777;padding-left:8px;display:flex;align-items:center}
.go{position:absolute;left:306px;top:56px;width:128px;height:21px;background:var(--blue);color:#fff;font-size:10px;display:flex;align-items:center;justify-content:center}
.arrow{width:22px;height:22px;border-radius:50%;background:rgba(255,255,255,.25);top:141px}
h3{font-size:13px;font-weight:400;color:var(--ink)}
p{font-size:7px;line-height:12px}
.tab{top:520px;height:19px;font-size:8px;font-weight:600}
.img{background:#555}
.news-img{top:606px;width:88px;height:64px}
.news h4{font-size:9px;font-weight:400;color:var(--ink)}
.news .date{font-size:6px;color:#333;margin:3px 0 5px}
.news p{font-size:6px;line-height:9px}
.news .more{font-size:6px;margin-top:6px;color:#888}
.band{left:62px;top:704px;width:632px;height:76px;background:linear-gradient(#0f4673,#0a3154)}
.box{top:866px;width:167px;height:104px;border:1px solid var(--line);padding:11px 13px}
.box h4{font-size:9px;font-weight:600;color:var(--ink);margin-bottom:6px}
.box p{font-size:6px;line-height:9.6px}
.box .cta{position:absolute;right:12px;bottom:10px;width:58px;height:15px;background:var(--navy);color:#fff;font-size:6.5px;display:flex;align-items:center;justify-content:center}
.box .cta.blue{background:var(--blue)}
.thumb{top:995px;width:73px;height:54px}
.footer{left:0;top:1088px;width:757px;height:112px;background:var(--navy)}
.fnav{left:62px;top:24px;display:flex;align-items:center;font-size:7px;color:#fff}
.fnav span.sep{margin:0 8px}
.fnav .pill{border:1px solid #fff;border-radius:10px;padding:3px 14px;margin-right:12px}
.social{top:26px;width:9px;height:9px;border-radius:50%;background:#fff}
.tip{left:637px;top:44px;width:40px;height:12px;border-radius:6px;background:var(--blue);color:#fff;font-size:5.5px;font-weight:700;display:flex;align-items:center;justify-content:center}
.fbot{top:76px;font-size:6px;color:#d8e2ec;display:flex;align-items:center;gap:6px}
.ico{width:13px;height:13px;border-radius:50%;background:#fff;display:flex;align-items:center;justify-content:center}
</style>
</head>
<body>
<div class="page">
  <div class="abs logo">Brightquay Trading</div>
  <div class="abs lang">Language: &nbsp; EN ▪ &nbsp;⌄</div>
  <div class="abs btn login">Login</div>
  <div class="abs btn join">Join Now</div>

  <nav class="abs nav">
    <a class="active">Home</a><a>About Us</a><a>Search</a><a>Directory</a><a>Subscribe</a><a>Services</a><a>General</a><a>Contact Us</a>
  </nav>

  <section class="abs hero" role="img" aria-label="Glowing world map with connection lines">
    <div class="abs arrow" style="left:20px"></div>
    <div class="abs arrow" style="left:593px"></div>
    <div class="abs panel">
      <h2>SEARCH TENDERS</h2>
      <div class="field" style="left:35px;width:128px">Enter keyword</div>
      <div class="field" style="left:170px;width:129px">Category <span style="margin-left:auto;margin-right:8px">⌄</span></div>
      <div class="go">Search</div>
    </div>
  </section>

  <h3 class="abs" style="left:62px;top:432px">Welcome To Our Site</h3>
  <p class="abs" style="left:64px;top:456px;width:342px">Sed malesuada vehicula nunc ut aliquam. Morbi eget risus odio. Morbi vel fermentum velit. Duis sit amet tincidunt sapien. Vestibulum vulputate mi a ornare convallis. Pellentesque cursus quis sem vel euismod. Nulla porttitor neque sed eros volutpat, accumsan viverra elit sodales. Mauris rhoncus nisl dolor, tincidunt porta odio bibendum consequat.</p>
  <div class="abs btn tab" style="left:64px;width:78px;background:var(--navy)">Tender</div>
  <div class="abs btn tab" style="left:146px;width:80px;background:var(--grey)">Entrepreneurs</div>
  <div class="abs img" role="img" aria-label="Course advert on black" style="left:438px;top:434px;width:74px;height:106px;background:#0a0a0a"></div>
  <div class="abs img" role="img" aria-label="University advert with newspaper" style="left:529px;top:434px;width:73px;height:106px;background:linear-gradient(#a8231d 0 20%,#b9b4ad 20%)"></div>
  <div class="abs img" role="img" aria-label="Online course advert with goggles" style="left:621px;top:434px;width:73px;height:106px;background:linear-gradient(#d7dadc,#8b8f90)"></div>

  <h3 class="abs" style="left:61px;top:580px">Latest News</h3>
  <div class="abs" style="left:668px;top:575px;width:11px;height:11px;border-radius:50%;background:#b5b8bb"></div>
  <div class="abs" style="left:683px;top:575px;width:11px;height:11px;border-radius:50%;background:var(--navy)"></div>

  <div class="abs img news-img" role="img" aria-label="Glowing stock market display" style="left:62px;background:linear-gradient(90deg,#1a0d08,#2f6b1f,#4a1a0a)"></div>
  <div class="abs news" style="left:157px;top:603px;width:112px">
    <h4>Lorem ipsum dolor sit</h4><div class="date">15/05/15 &nbsp;-&nbsp; Friday</div>
    <p>Pellentesque laoreet iaculis tempor. Sed ultricies ullamcorper magna, vel tempus lacus dapibus ac.</p><div class="more">Read More ◦</div>
  </div>
  <div class="abs img news-img" role="img" aria-label="Businessman breaking chains" style="left:277px;background:linear-gradient(#1c2430,#56606c)"></div>
  <div class="abs news" style="left:372px;top:603px;width:112px">
    <h4>Lorem ipsum dolor sit</h4><div class="date">15/05/15 &nbsp;-&nbsp; Friday</div>
    <p>Pellentesque laoreet iaculis tempor. Sed ultricies ullamcorper magna, vel tempus lacus dapibus ac.</p><div class="more">Read More ◦</div>
  </div>
  <div class="abs img news-img" role="img" aria-label="Businessman facing digital screen" style="left:492px;background:linear-gradient(90deg,#27507a,#b6764a,#2d5b86)"></div>
  <div class="abs news" style="left:587px;top:603px;width:112px">
    <h4>Lorem ipsum dolor sit</h4><div class="date">15/05/15 &nbsp;-&nbsp; Friday</div>
    <p>Pellentesque laoreet iaculis tempor. Sed ultricies ullamcorper magna, vel tempus lacus dapibus ac.</p><div class="more">Read More ◦</div>
  </div>

  <section class="abs band">
    <div class="abs" style="left:53px;top:30px;font-size:13.5px;color:#fff">Lorem ipsum dolor sit amet, consectetur adipiscing elit.</div>
    <div class="abs btn" style="left:413px;top:24px;width:142px;height:27px;background:var(--blue);font-size:9.5px">Join Now</div>
  </section>

  <h3 class="abs" style="left:61px;top:801px">Access Types</h3>
  <p class="abs" style="left:62px;top:826px;width:356px;font-size:7px;line-height:10px">Access to the website will be based on the type of access that is requested, i.e. Basic or Advances access.</p>
  <div class="abs img" role="img" aria-label="University MBA advert banner" style="left:438px;top:827px;width:256px;height:60px;background:linear-gradient(90deg,#eef0f2,#c9ccd0)"></div>

  <div class="abs box" style="left:62px">
    <h4>Lite Access</h4>
    <p>only allows a user to register, create a profile and view tender information of that day. Previously loaded tender information will not be visible with this type of access.</p>
    <div class="cta">Access Now</div>
  </div>
  <div class="abs box" style="left:245px">
    <h4>Premium Access</h4>
    <p>will be based on subscriptions of 3, 6, 12 or 24 months and will allow users to have access to all tender information, search facilities, disable profile from being visible to other users.</p>
    <div class="cta blue">Access Now</div>
  </div>

  <div class="abs img thumb" role="img" aria-label="Drink advert in blue" style="left:62px;background:#2a86c8"></div>
  <div class="abs img thumb" role="img" aria-label="Ski goggles product shot" style="left:155px;background:linear-gradient(#eef2f4,#b8c2c8)"></div>
  <div class="abs img thumb" role="img" aria-label="Food product advert" style="left:249px;background:linear-gradient(#efe4c8,#b79b66)"></div>
  <div class="abs img thumb" role="img" aria-label="Bottles splashing in water" style="left:342px;background:linear-gradient(#0b4f9a,#1d7ad0)"></div>
  <div class="abs img thumb" role="img" aria-label="Degree course advert" style="left:434px;background:linear-gradient(90deg,#f3f3f3,#d8dccd)"></div>
  <div class="abs img thumb" role="img" aria-label="Design contest advert" style="left:528px;background:#2c2c2c"></div>
  <div class="abs img thumb" role="img" aria-label="University sales course advert" style="left:622px;background:linear-gradient(#8a8a6a,#4d5358)"></div>

  <footer class="abs footer">
    <div class="abs fnav">
      <span class="pill">Home</span>About Us<span class="sep">|</span>Search<span class="sep">|</span>Directory<span class="sep">|</span>Subscribe<span class="sep">|</span>Services<span class="sep">|</span>General<span class="sep">|</span>Contact Us
    </div>
    <div class="abs social" style="left:633px"></div>
    <div class="abs social" style="left:651px"></div>
    <div class="abs social" style="left:669px"></div>
    <div class="abs social" style="left:689px"></div>
    <div class="abs tip">PINWHEEL</div>
    <div class="abs fbot" style="left:62px;top:72px">
      <span class="ico"><svg width="7" height="8" viewBox="0 0 7 8"><path d="M3.5 0A3 3 0 0 0 .5 3c0 2 3 5 3 5s3-3 3-5a3 3 0 0 0-3-3z" fill="#0d3356"/><circle cx="3.5" cy="3" r="1" fill="#fff"/></svg></span>
      <span style="line-height:9px">14 Harbour Lane, Marina Park,<br>Eastbay 4021</span>
    </div>
    <div class="abs fbot" style="left:275px">
      <span class="ico"><svg width="7" height="7" viewBox="0 0 7 7"><path d="M1 .5l1.5 0 .7 1.6-.9.7a4 4 0 0 0 1.9 1.9l.7-.9 1.6.7V6A.8.8 0 0 1 5.7 6.8 5.8 5.8 0 0 1 .2 1.3.8.8 0 0 1 1 .5z" fill="#0d3356"/></svg></span>+ 27 31 555 0148
    </div>
    <div class="abs fbot" style="left:357px">
      <span class="ico"><svg width="7" height="5" viewBox="0 0 7 5"><rect width="7" height="5" rx=".6" fill="#0d3356"/><path d="M.4.5 3.5 3 6.6.5" stroke="#fff" stroke-width=".7" fill="none"/></svg></span>info@brightquay-mail.org
    </div>
    <div class="abs fbot" style="left:550px">©Copyright 2015 brightquay. All Rights Reserved.</div>
  </footer>
</div>
</body>
</html>
```